KB Rubbish Removal Business Card

Hey,
I need a double sided business card designed for a rubbish removal business based in Australia. Logo is already chosen, similar colours preferred for both sides of the business card.

Details to include:

Front:

KB Rubbish Removal
Darren Holloway
Managing Director
Mobile: 0471 902 146
Email: darren@kbrubbishremoval.com.au
Website: kbrubbishremoval.com.au

Rear:

How did we do?
kbrubbishremoval.com.au/review

```html
<!DOCTYPE html>
<html lang="en">
<head>
<meta charset="utf-8">
<title>KB Rubbish Removal – Business Card</title>
<link rel="stylesheet" href="https://fonts.googleapis.com/css2?family=Roboto:wght@500;700;900&family=Roboto+Condensed:wght@400&display=swap">
<style>
  :root {
    --canvas: #efefef;
    --white: #ffffff;
    --green-light: #17a83a;
    --green-mid: #128a2c;
    --green-deep: #0a6a1d;
    --green-name: #0e6b1f;
    --orange: #f26a3a;
    --grey-text: #5a5a5a;
    --card-edge: #d6e6d6;
  }
  * { margin: 0; padding: 0; box-sizing: border-box; }
  html, body { width: 1200px; height: 1200px; overflow: hidden; }
  body {
    background: var(--canvas);
    position: relative;
    font-family: "Roboto", Arial, sans-serif;
  }
  .card {
    position: absolute;
    left: 178px;
    width: 842px;
    height: 481px;
    overflow: hidden;
    box-shadow: 0 1px 3px rgba(0,0,0,0.12);
  }
  .card--front { top: 69px; background: var(--white); border: 1px solid var(--card-edge); }
  .card--back { top: 648px; }

  .front-band { position: absolute; inset: 0; width: 100%; height: 100%; }

  .brand-mark {
    position: absolute;
    left: 359px; top: 37px;
    width: 122px; height: 122px;
    border-radius: 50%;
    background: var(--green-mid);
  }
  .brand-name {
    position: absolute; left: 0; right: 0; top: 193px;
    text-align: center;
    color: var(--orange);
    font-weight: 700;
    font-size: 37px;
    letter-spacing: 0.5px;
  }
  .person-name {
    position: absolute; left: 0; right: 0; top: 255px;
    text-align: center;
    color: var(--green-name);
    font-weight: 900;
    font-size: 23px;
    letter-spacing: 0.6px;
  }
  .person-role {
    position: absolute; left: 0; right: 0; top: 290px;
    text-align: center;
    color: var(--grey-text);
    font-weight: 700;
    font-size: 15px;
    letter-spacing: 1.2px;
  }
  .contact-list {
    position: absolute; left: 32px; right: 30px; top: 406px;
    display: flex; justify-content: space-between; align-items: center;
    list-style: none;
    font-family: "Roboto Condensed", "Arial Narrow", sans-serif;
    font-size: 21px;
    color: var(--white);
  }
  .contact-item { display: flex; align-items: center; gap: 6px; white-space: nowrap; }
  .contact-icon { width: 20px; height: 20px; flex: none; }

  .back-pattern {
    position: absolute; inset: 0;
    background: linear-gradient(90deg, var(--green-mid) 0%, var(--green-light) 55%, var(--green-deep) 100%);
  }
  .review-mark {
    position: absolute; left: 64px; top: 379px;
    width: 54px; height: 54px;
    border-radius: 50%;
    background: var(--white);
  }
  .review-prompt {
    position: absolute; left: 143px; top: 378px;
    color: var(--white);
    font-weight: 700;
    font-size: 19px;
  }
  .review-url {
    position: absolute; left: 142px; top: 402px;
    color: var(--white);
    font-family: "Roboto Condensed", "Arial Narrow", sans-serif;
    font-size: 29px;
  }
</style>
</head>
<body>

<section class="card card--front">
  <svg class="front-band" viewBox="0 0 842 481" preserveAspectRatio="none" aria-hidden="true">
    <defs>
      <radialGradient id="bandGradient" cx="0.3" cy="0.55" r="0.9">
        <stop offset="0" stop-color="#0c7422"/>
        <stop offset="1" stop-color="#17a83a"/>
      </radialGradient>
    </defs>
    <path d="M0 212 Q421 474 842 212 L842 481 L0 481 Z" fill="url(#bandGradient)"/>
  </svg>

  <div class="brand-mark" aria-hidden="true"></div>
  <h1 class="brand-name">KB RUBBISH REMOVAL</h1>
  <p class="person-name">DARREN HOLLOWAY</p>
  <p class="person-role">MANAGING DIRECTOR</p>

  <ul class="contact-list">
    <li class="contact-item">
      <svg class="contact-icon" viewBox="0 0 20 20" aria-hidden="true">
        <circle cx="10" cy="10" r="10" fill="#f26a3a"/>
        <path d="M6.5 5.5l2 0 .8 2.4-1.2 1a6 6 0 0 0 3 3l1-1.2 2.4.8 0 2a1 1 0 0 1-1 1A8.5 8.5 0 0 1 5.5 6.5a1 1 0 0 1 1-1z" fill="#fff"/>
      </svg>
      0471 902 146
    </li>
    <li class="contact-item">
      <svg class="contact-icon" viewBox="0 0 20 20" aria-hidden="true">
        <circle cx="10" cy="10" r="10" fill="#f26a3a"/>
        <rect x="5" y="6.5" width="10" height="7" rx="1" fill="#fff"/>
        <path d="M5.5 7l4.5 3.5L14.5 7" fill="none" stroke="#f26a3a" stroke-width="1"/>
      </svg>
      darren@kbrubbishremoval.com.au
    </li>
    <li class="contact-item">
      <svg class="contact-icon" viewBox="0 0 20 20" aria-hidden="true">
        <circle cx="10" cy="10" r="10" fill="#f26a3a"/>
        <circle cx="10" cy="10" r="5" fill="none" stroke="#fff" stroke-width="1.2"/>
        <path d="M5 10h10M10 5c-2.5 3-2.5 7 0 10M10 5c2.5 3 2.5 7 0 10" fill="none" stroke="#fff" stroke-width="1"/>
      </svg>
      kbrubbishremoval.com.au
    </li>
  </ul>
</section>

<section class="card card--back">
  <div class="back-pattern" role="img" aria-label="Green background with a repeating brand symbol pattern"></div>
  <div class="review-mark" aria-hidden="true"></div>
  <p class="review-prompt">How did we do?</p>
  <p class="review-url">kbrubbishremoval.com.au/review</p>
</section>

</body>
</html>
```